Medical Marihuana Ziplock Bag Mockup Design

We seek skilled and professional designer for medical marihuana ziplock bag packaging design. We need a modern, minimal, clean Design with the name productname: Plumo - Feinschnitt will be a ziplock bag (see attachment) samples.
Product may but must not contain a cannabis leaf in Design7Logo

Target Market(s)

young audience

Industry/Entity Type

Medical

Logo Text

P L U M O

Font styles to use
Serif
Sans Serif

Colors
9bcb3c
abd037
cadf82
ffc214
fece3e
fee18a
6b449b
886aae
b8a6cd

Requirements
Nice to have
• Can but must not contain a minimal cannabis leaf as abstract sign

```html
<!DOCTYPE html>
<html lang="de">
<head>
<meta charset="utf-8">
<title>Plumo Feinschnitt – Pouch Range</title>
<link rel="stylesheet" href="https://fonts.googleapis.com/css2?family=Open+Sans:wght@400;500;800&display=swap">
<style>
  :root {
    --canvas: #ffffff;
    --leaf-light: #bfe08f;
    --leaf-mid: #5ec46a;
    --leaf-deep: #1f9a48;
    --forest: #1b8a3f;
    --lime: #d5e0a9;
    --lavender: #c8c2dc;
    --cream: #ece6b8;
    --brand-green: #1b8a3f;
    --ink: #1a1a1a;
    --white: #ffffff;
  }
  * { margin: 0; padding: 0; box-sizing: border-box; }
  html, body { width: 1200px; height: 1062px; overflow: hidden; background: var(--canvas); }
  .stage { position: relative; width: 1200px; height: 1062px; }

  .pouch {
    position: absolute;
    top: 425px;
    width: 240px;
    height: 385px;
    border-radius: 6px;
    overflow: hidden;
    background: var(--pouch-colour);
    color: var(--text-colour);
    font-family: "Open Sans", Arial, sans-serif;
  }
  .pouch--forest   { left: 197px; --pouch-colour: var(--forest);   --text-colour: var(--cream);       --box-colour: var(--white); }
  .pouch--lime     { left: 487px; --pouch-colour: var(--lime);     --text-colour: var(--brand-green); --box-colour: var(--ink); }
  .pouch--lavender { left: 759px; --pouch-colour: var(--lavender); --text-colour: var(--brand-green); --box-colour: var(--ink); }

  .pouch__foliage {
    position: absolute; left: 0; top: 0; width: 100%; height: 127px;
    background:
      linear-gradient(180deg, rgba(255,255,255,0) 55%, var(--white) 100%),
      linear-gradient(100deg, var(--leaf-light) 0%, var(--leaf-mid) 45%, var(--leaf-light) 65%, var(--leaf-deep) 100%);
  }

  .pouch__name {
    position: absolute; left: 0; width: 100%; top: 186px;
    text-align: center;
    font-size: 29px; font-weight: 800; line-height: 1; letter-spacing: 0.5px;
  }
  .pouch__variety {
    position: absolute; left: 0; width: 100%; top: 219px;
    text-align: center; font-size: 13px; font-weight: 500; letter-spacing: 0.4px;
  }

  .pouch__origin {
    position: absolute; left: 0; width: 100%; top: 242px;
    text-align: center; font-size: 11.5px; font-weight: 500; letter-spacing: 0.2px;
  }

  .pouch__warning {
    position: absolute; left: 44px; top: 294px; width: 152px; height: 77px;
    border: 2.5px solid var(--box-colour);
    color: var(--box-colour);
    font-size: 7.6px; line-height: 10px; text-align: center;
    padding: 4px 3px 0;
  }
</style>
</head>
<body>
<main class="stage">

  <section class="pouch pouch--forest">
    <div class="pouch__foliage" role="img" aria-label="Illustration of hemp leaves fanning down from the top edge"></div>
    <h1 class="pouch__name">PLUMO</h1>
    <p class="pouch__variety">FEINSCHNITT</p>
    <p class="pouch__origin">100% SCHWEIZER HANF</p>
    <p class="pouch__warning">Rauchen fügt Ihnen und den Menschen in Ihrer Umgebung erheblichen Schaden zu. Fumer nuit gravement à votre santé et à celle de votre entourage. Il fumo danneggia gravemente te e chi ti sta intorno.</p>
  </section>

  <section class="pouch pouch--lime">
    <div class="pouch__foliage" role="img" aria-label="Illustration of hemp leaves fanning down from the top edge"></div>
    <h2 class="pouch__name">PLUMO</h2>
    <p class="pouch__variety">FEINSCHNITT</p>
    <p class="pouch__origin">100% SCHWEIZER HANF</p>
    <p class="pouch__warning">Rauchen fügt Ihnen und den Menschen in Ihrer Umgebung erheblichen Schaden zu. Fumer nuit gravement à votre santé et à celle de votre entourage. Il fumo danneggia gravemente te e chi ti sta intorno.</p>
  </section>

  <section class="pouch pouch--lavender">
    <div class="pouch__foliage" role="img" aria-label="Illustration of hemp leaves fanning down from the top edge"></div>
    <h2 class="pouch__name">PLUMO</h2>
    <p class="pouch__variety">FEINSCHNITT</p>
    <p class="pouch__origin">100% SCHWEIZER HANF</p>
    <p class="pouch__warning">Rauchen fügt Ihnen und den Menschen in Ihrer Umgebung erheblichen Schaden zu. Fumer nuit gravement à votre santé et à celle de votre entourage. Il fumo danneggia gravemente te e chi ti sta intorno.</p>
  </section>

</main>
</body>
</html>
```